Flyer für KFZ-Gutachter
Zielgruppe
NFZ und KFZ Gutachten. Firma ist neu gegründet und Flyer wird benötigt um sich bei Werkstätten, Versicherungen und Privatkunden vorzustellen.
Aufgabenstellung
Es soll elegant, klassisch sein und angelehnt sein an meine Website https://www.holvarentis.de/ Handynummer 0157 - 62830417 bitte einpflegen. Außerdem sollten die Logos des Bundesverbandes und der Zertifizierung mit im Flyer eingebunden werden. Diese lade ich hoch. Auch das korrekte Logo lade ich hoch.

```html
<!DOCTYPE html>
<html lang="de">
<head>
<meta charset="utf-8">
<title>Holvarentis Stuttgart – Flyer</title>
<link rel="stylesheet" href="https://fonts.googleapis.com/css2?family=Lexend:wght@600;700&family=Poppins:wght@400;500;600;700&display=swap">
<style>
  :root {
    --ink: #0c0c0c;
    --night: #151515;
    --white: #ffffff;
    --paper: #e9e9ea;
    --banner: #cfcfcf;
    --stage: #dcdcdc;
    --muted: #3a3a3a;
    --shadow: #bdbdbd;
    --badge: #d9d9d9;
  }
  * { box-sizing: border-box; margin: 0; padding: 0; }
  html, body { width: 1200px; height: 1117px; overflow: hidden; }
  body {
    background: var(--stage);
    font-family: "Poppins", sans-serif;
    display: flex; align-items: center; justify-content: center;
  }
  .flyer {
    position: relative;
    width: 762px; height: 1077px;
    background: var(--night);
    overflow: hidden;
    color: var(--white);
  }
  .hero-photo {
    position: absolute;
    background: linear-gradient(135deg, #3c4550, #1c1f24 70%, #0e0e0e);
  }
  .hero-photo--inspector { left: 0; top: 0; width: 270px; height: 240px; }
  .hero-photo--checklist {
    left: 500px; top: 150px; width: 262px; height: 175px;
    background: linear-gradient(135deg, #5b6470, #26303b 60%, #121212);
  }
  .hero-backdrop {
    position: absolute; left: 0; top: 240px; width: 762px; height: 360px;
    background: linear-gradient(180deg, #1d1d1d, #2b2b2b 60%, #1a1a1a);
  }
  .brand-box {
    position: absolute; left: 255px; top: 70px; width: 250px; height: 250px;
    background: var(--white);
    color: var(--ink);
    display: flex; flex-direction: column; align-items: center; justify-content: center;
    gap: 10px;
  }
  .brand-box__mark { width: 34px; height: 34px; border: 3px solid var(--ink); }
  .brand-box__name { font-weight: 600; font-size: 30px; line-height: 1; letter-spacing: 0.5px; }
  .brand-box__city { font-weight: 600; font-size: 14px; letter-spacing: 9px; margin-left: 9px; }
  .headline {
    position: absolute; left: 0; top: 340px; width: 762px;
    font-family: "Lexend", sans-serif; font-weight: 700;
    font-size: 38px; line-height: 1.05; text-align: center; text-transform: uppercase;
  }
  .tagline {
    position: absolute; left: 140px; top: 436px; width: 482px; height: 30px;
    background: var(--banner); color: var(--ink);
    font-weight: 700; font-size: 15.5px; letter-spacing: 0.3px;
    display: flex; align-items: center; justify-content: center; text-transform: uppercase;
  }
  .intro {
    position: absolute; left: 80px; top: 474px; width: 602px;
    font-size: 12.5px; line-height: 1.45; text-align: center;
  }
  .certification {
    position: absolute; left: 0; top: 520px; width: 762px;
    font-weight: 700; font-size: 13px; text-align: center;
  }
  .partner-badge {
    position: absolute; top: 512px; width: 34px; height: 34px;
    border-radius: 50%; background: var(--badge);
  }
  .partner-badge--association { left: 160px; }
  .partner-badge--certificate { left: 568px; }
  .content-wave { position: absolute; left: 0; top: 540px; }
  .services {
    position: absolute; left: 42px; top: 562px; width: 678px;
    display: grid; grid-template-columns: repeat(3, 1fr); gap: 16px;
  }
  .service-card {
    background: var(--white); color: var(--ink);
    padding: 8px 8px 16px;
    box-shadow: 8px 8px 0 var(--shadow);
    text-align: center; height: 280px;
  }
  .service-card__photo { height: 150px; margin-bottom: 12px; }
  .service-card__photo--accident { background: linear-gradient(135deg, #d8d8d8, #6a6a6a 50%, #c0262a); }
  .service-card__photo--classic { background: linear-gradient(135deg, #8c8a86, #d8d5cf 50%, #4a4846); }
  .service-card__photo--damage { background: linear-gradient(160deg, #9cc2e6, #3c6fb0 45%, #6c7278); }
  .service-card__title { font-weight: 700; font-size: 15px; margin-bottom: 6px; }
  .service-card__text { font-size: 11px; line-height: 1.4; color: var(--muted); padding: 0 10px; }
  .about {
    position: absolute; left: 0; top: 870px; width: 762px; height: 92px;
    color: var(--ink); text-align: center;
  }
  .about__title { font-weight: 700; font-size: 14.5px; text-transform: uppercase; margin-bottom: 5px; }
  .about__text { font-size: 11.5px; line-height: 1.45; padding: 0 70px; margin-bottom: 4px; }
  .contact-bar {
    position: absolute; left: 0; top: 970px; width: 762px; height: 107px;
    background: var(--ink);
    display: flex; align-items: center; justify-content: center; gap: 36px;
  }
  .contact-bar__group { display: flex; flex-direction: column; gap: 8px; }
  .contact-bar__divider { width: 1px; height: 56px; background: #777; }
  .contact-item { display: flex; align-items: center; gap: 10px; font-weight: 500; font-size: 15.5px; white-space: nowrap; }
  .contact-item svg { width: 16px; height: 16px; flex: none; }
</style>
</head>
<body>
  <main class="flyer">
    <div class="hero-backdrop" role="img" aria-label="Dunkles Foto einer Werkstatthalle"></div>
    <div class="hero-photo hero-photo--inspector" role="img" aria-label="Foto: Gutachter im Anzug prüft ein Fahrzeug an der geöffneten Tür"></div>
    <div class="hero-photo hero-photo--checklist" role="img" aria-label="Foto: Hände füllen ein Prüfprotokoll auf einem Klemmbrett im Fahrzeug aus"></div>

    <div class="brand-box">
      <div class="brand-box__mark"></div>
      <div class="brand-box__name">HOLVARENTIS</div>
      <div class="brand-box__city">STUTTGART</div>
    </div>

    <h1 class="headline">Ihr Experte für Gutachten<br>in Stuttgart</h1>
    <div class="tagline">Präzise Bewertungen für Ihre Bedürfnisse</div>
    <p class="intro">Wir sind spezialisiert auf die Erstellung von Gutachten für Nutzfahrzeuge, Kraftfahrzeugschäden und Bewertungen. Vertrauen Sie auf unsere Expertise!</p>
    <div class="partner-badge partner-badge--association" role="img" aria-label="Platz für das Zeichen des Bundesverbandes"></div>
    <p class="certification">| Sachverständige Zertifiziert nach DIN ISO/EN 17024 |</p>
    <div class="partner-badge partner-badge--certificate" role="img" aria-label="Platz für das Zertifizierungszeichen"></div>

    <svg class="content-wave" width="762" height="440" viewBox="0 0 762 440" aria-hidden="true">
      <path d="M0 40 Q381 -10 762 40 L762 440 L0 440 Z" fill="#ffffff"/>
      <path d="M0 300 Q381 250 762 300 L762 440 L0 440 Z" fill="#e9e9ea"/>
    </svg>

    <section class="services">
      <article class="service-card">
        <div class="service-card__photo service-card__photo--accident" role="img" aria-label="Foto: zwei verunfallte Autos, weiß und rot"></div>
        <h2 class="service-card__title">Unfallgutachten</h2>
        <p class="service-card__text">Wir erstellen detaillierte Unfallgutachten, die Ihnen bei der Schadensregulierung helfen und für Versicherungen präzise nachvollziehbar sind.</p>
      </article>
      <article class="service-card">
        <div class="service-card__photo service-card__photo--classic" role="img" aria-label="Foto: silberner Oldtimer in Nahaufnahme"></div>
        <h2 class="service-card__title">Wertgutachten</h2>
        <p class="service-card__text">Erhalten Sie fundierte Wertgutachten, die Ihnen bei Kaufentscheidungen oder bei der Schadenregulierung nützlich sein können.</p>
      </article>
      <article class="service-card">
        <div class="service-card__photo service-card__photo--damage" role="img" aria-label="Foto: zwei Männer begutachten ein beschädigtes blaues Auto"></div>
        <h2 class="service-card__title">Schadensgutachten</h2>
        <p class="service-card__text">Präzise Schadensgutachten, die alle relevanten Informationen enthalten und die rechtlichen Anforderungen erfüllen.</p>
      </article>
    </section>

    <section class="about">
      <h2 class="about__title">Ihre zuverlässigen Sachverständigen vor Ort</h2>
      <p class="about__text">Wir sind Ihr kompetenter Partner in Stuttgart und bieten Ihnen umfassende Gutachterdienstleistungen für Nutzfahrzeuge, Kraftfahrzeugschäden- und Bewertung.</p>
      <p class="about__text">Unser Ziel ist es, Ihnen in jeder Situation den bestmöglichen Service zu bieten.</p>
    </section>

    <footer class="contact-bar">
      <div class="contact-bar__group">
        <div class="contact-item">
          <svg viewBox="0 0 16 16"><circle cx="8" cy="8" r="8" fill="#fff"/><path d="M5.2 4.2l1.4-.3.8 1.9-.9.7c.4.9 1.1 1.6 2 2l.7-.9 1.9.8-.3 1.4c-3 .2-5.8-2.6-5.6-5.6z" fill="#0c0c0c"/></svg>
          <span>0157 - 62830417</span>
        </div>
        <div class="contact-item">
          <svg viewBox="0 0 16 16"><circle cx="8" cy="8" r="7.2" fill="none" stroke="#fff" stroke-width="1.4"/><rect x="4.3" y="5.3" width="7.4" height="5.4" fill="none" stroke="#fff" stroke-width="1.1"/><path d="M4.3 5.3L8 8.3l3.7-3" fill="none" stroke="#fff" stroke-width="1.1"/></svg>
          <span>info@holvarentis.de</span>
        </div>
      </div>
      <div class="contact-bar__divider"></div>
      <div class="contact-bar__group">
        <div class="contact-item">
          <svg viewBox="0 0 16 16"><circle cx="8" cy="8" r="7" fill="none" stroke="#fff" stroke-width="1.4"/><ellipse cx="8" cy="8" rx="3" ry="7" fill="none" stroke="#fff" stroke-width="1.1"/><path d="M1 8h14M2.2 4.5h11.6M2.2 11.5h11.6" stroke="#fff" stroke-width="1.1"/></svg>
          <span>www.holvarentis.de</span>
        </div>
        <div class="contact-item">
          <svg viewBox="0 0 16 16"><path d="M8 15S3 9.6 3 6a5 5 0 0 1 10 0c0 3.6-5 9-5 9z" fill="none" stroke="#fff" stroke-width="1.5"/><circle cx="8" cy="6" r="1.8" fill="#fff"/></svg>
          <span>Ahornstr. 18 - 71642 Ludwigsburg</span>
        </div>
      </div>
    </footer>
  </main>
</body>
</html>
```